Brightwell Assist Public Benefit Corporation - Initial Website

We need to develop an initial website for Brightwell Assist PBC. We are a startup managed business services provider focused on small business owners, entrepreneurs and their employees. We are a public benefit corporation and our public mission is to help business owners, entrepreneurs and their employees overcome the challenges that hold them back from reaching personal and professional success.
Our primary service offerings are managed business services that allow us to support the day-to-day operations of the businesses we support. This ongoing support provides the necessary pre-requisite relationship so we can provide effective and timely support when their organizations are experiencing challenges and moments of crisis. In those moments, it is our opportunity to help them overcome those challenges and stay on track for business utopia.
Our services are provided on a contract basis for a fixed monthly fee. We want to build strong relationships that help our clients grow their businesses while taking away the stresses associated with the backend of the business operations.
Finally, our public benefit is that we provide crisis invention, critical incident support, and mental health services to business owners and their employees during challenging times in an effort to improve their overall quality of life.

Coding

Coded - Design and coding required

```html
<!DOCTYPE html>
<html lang="en">
<head>
<meta charset="utf-8">
<title>Brightwell Assist PBC</title>
<link href="https://fonts.googleapis.com/css2?family=Poppins:wght@400;500;600;700&display=swap" rel="stylesheet">
<style>
:root{
  --orange:#f97316;
  --navy:#0b1b4d;
  --ink:#111827;
  --text:#4b5563;
  --muted:#6b7280;
  --line:#e5e7eb;
  --soft:#f3f4f6;
  --slate:#b4c1cd;
}
*{margin:0;padding:0;box-sizing:border-box}
html,body{width:1200px;height:4743px;overflow:hidden}
body{font-family:"Poppins",sans-serif;color:var(--ink);background:#fff;position:relative}
.abs{position:absolute}
.label{font-size:11px;color:var(--orange);text-transform:uppercase;letter-spacing:.3px;display:flex;align-items:center;gap:8px}
.label::before{content:"";width:7px;height:7px;border-radius:50%;background:var(--orange)}
.h2{font-size:36px;font-weight:500;line-height:1.32;color:var(--ink)}
.btn{display:inline-flex;align-items:center;justify-content:center;border-radius:20px;font-size:12px;font-weight:500}
.btn-orange{background:var(--orange);color:#fff}
.brand{font-size:26px;font-weight:500;color:var(--orange);line-height:1}
.brand-sub{font-size:9px;font-weight:600;color:var(--navy);letter-spacing:.2px;margin-top:3px}

/* header */
.site-header{left:0;top:0;width:1200px;height:80px;background:#fff;box-shadow:0 1px 4px rgba(0,0,0,.06);z-index:3}
.nav{left:452px;top:32px;display:flex;gap:48px;font-size:12px;color:var(--ink)}
.nav span::after{content:" ▾";font-size:9px}
.header-cta{left:924px;top:22px;width:135px;height:36px}

/* hero */
.hero-bg{left:0;top:80px;width:1200px;height:573px;background:linear-gradient(90deg,#f4f6f9 0%,#e8edf3 40%,#b7c6d8 65%,#2c4676 100%)}
.hero-title{left:138px;top:218px;font-size:56px;font-weight:700;line-height:1.13;color:var(--ink)}
.hero-text{left:138px;top:364px;width:500px;font-size:14px;line-height:1.8;color:#1f2937}
.hero-btn1{left:138px;top:441px;width:134px;height:36px}
.hero-btn2{left:292px;top:441px;width:204px;height:36px;border:1.5px solid var(--navy);color:var(--navy);background:#fff}

.goal{left:0;top:653px;width:1200px;height:152px;border-bottom:1px solid var(--line);display:flex;align-items:center;justify-content:center;font-size:15px;color:var(--text)}
.goal b{color:var(--orange);font-weight:500;margin-left:5px}

/* services */
.svc-head{left:138px;top:878px;font-size:36px}
.stat{top:872px;width:204px;border-bottom:1px solid var(--line);padding-bottom:14px}
.stat-num{font-size:50px;font-weight:500;color:var(--orange);line-height:1.1;display:flex;gap:14px}
.stat-num small{font-size:12px;color:var(--ink);font-weight:400;margin-top:8px}
.stat-note{font-size:12px;line-height:1.6;color:var(--ink);margin-top:28px}
.svc-card{top:1063px;width:288px;text-align:center}
.svc-photo{height:150px;box-shadow:0 4px 10px rgba(0,0,0,.12)}
.svc-title{font-size:15px;font-weight:500;margin-top:28px}
.svc-desc{font-size:11.5px;color:var(--text);line-height:1.6;margin:10px 30px 0}
.view-all{left:510px;top:1349px;display:flex;align-items:center;gap:16px;font-size:14px;font-weight:500}
.arrow-circ{width:38px;height:38px;border-radius:50%;background:var(--orange);display:flex;align-items:center;justify-content:center}
.building{left:935px;top:1288px;width:265px;height:190px;background:linear-gradient(135deg,#d1d5db,#4b5563);clip-path:polygon(100% 0,100% 100%,0 100%,40% 55%)}

/* about */
.about{left:0;top:1478px;width:1200px;height:559px;background:var(--soft)}
.about-frame{left:127px;top:1562px;width:438px;height:360px;border-top:15px solid var(--orange);border-left:15px solid var(--orange)}
.about-photo{left:142px;top:1577px;width:438px;height:363px;background:linear-gradient(135deg,#e9e4dc,#c9b89e 50%,#8a7662)}
.about-copy{left:626px;top:1572px;width:440px}
.about-copy p{font-size:12.5px;line-height:1.82;color:#1f2937;margin-top:14px}

/* testimonials */
.testi{left:0;top:2037px;width:1200px;height:576px;background:var(--slate)}
.testi-title{left:0;top:2124px;width:1200px;text-align:center;color:#fff}
.testi-title .label{justify-content:center;color:#fff}
.testi-title .label::before{background:#fff}
.testi-title h2{color:#fff;margin-top:10px}
.t-card{top:2234px;height:224px;background:#fff;padding:28px 30px}
.t-name{font-size:16px;font-weight:600}
.t-role{font-size:11px;color:var(--muted);margin-top:2px}
.t-stars{position:absolute;top:30px;color:var(--orange);font-size:14px;letter-spacing:1px}
.t-body{font-size:11.5px;line-height:1.65;color:var(--text);margin-top:22px;width:280px}
.avatar{top:2256px;width:74px;height:74px;border-radius:50%;background:linear-gradient(135deg,#e5e7eb,#9ca3af);border:3px solid #fff}
.dots{left:567px;top:2506px;display:flex;gap:8px}
.dots i{width:10px;height:10px;border-radius:50%;background:#fff;opacity:.75}
.dots i:first-child{opacity:1}

/* why */
.why-head{left:0;top:2708px;width:1200px;text-align:center}
.why-head .label{justify-content:center}
.why-head h2{margin-top:10px}
.why-text{left:150px;top:2848px;width:900px;text-align:center;font-size:12.5px;line-height:1.8;color:#1f2937}
.feature{width:276px;height:78px;border:1.5px solid var(--line);display:flex;align-items:center;gap:18px;padding-left:22px;font-size:14px;font-weight:500}
.f-icon{width:46px;height:46px;border-radius:50%;display:flex;align-items:center;justify-content:center}
.f-o{background:var(--orange)}.f-n{background:var(--navy)}

/* contact */
.contact{left:0;top:3248px;width:1200px;height:622px;background:var(--navy)}
.contact-head{left:138px;top:3345px}
.contact-head h2{color:#fff;font-size:38px;margin-top:10px;line-height:1.28}
.map{left:718px;top:3356px;width:368px;height:150px;background:radial-gradient(ellipse at center,#ffffff 0%,#c7cfe0 55%,rgba(11,27,77,0) 72%);opacity:.9}
.quote-card{left:142px;top:3581px;width:916px;height:563px;background:#fff;border-radius:14px;box-shadow:0 6px 20px rgba(0,0,0,.1);overflow:hidden}
.quote-photo{left:0;top:0;width:352px;height:563px;background:linear-gradient(160deg,#eef0f3,#b9c3d4 55%,#3b4f86)}
.quote-form{left:403px;top:40px;width:465px}
.quote-form h3{font-size:28px;font-weight:600}
.field{margin-top:22px}
.field label{font-size:12.5px;font-weight:500;display:block;margin-left:6px}
.field label em{color:var(--orange);font-style:normal}
.input{height:43px;background:var(--soft);border:1px solid #eceef1;border-radius:4px;margin-top:10px;font-size:11px;color:#9ca3af;padding:0 20px;display:flex;align-items:center}
.input.filled{color:var(--ink)}
.submit{margin-top:36px;height:50px;background:var(--orange);color:#fff;border-radius:5px;display:flex;align-items:center;justify-content:center;font-size:11px;font-weight:600}

/* footer */
.foot-brand{left:138px;top:4330px}
.foot-tag{left:399px;top:4338px;width:470px;font-size:12.5px;line-height:1.7;color:#1f2937}
.social{top:4334px;width:34px;height:34px;border-radius:50%}
.foot-line{left:138px;width:922px;height:1px;background:#d1d5db}
.foot-info-title{left:0;top:4450px;width:1200px;text-align:center;font-size:13px;font-weight:500}
.info-col{top:4508px;width:260px;text-align:center}
.info-col .lbl{font-size:12px;font-weight:500;margin-top:10px}
.info-col .val{font-size:12px;color:var(--text);line-height:1.6;margin-top:18px}
.vdiv{top:4502px;width:1px;height:118px;background:#d1d5db}
.copy{left:138px;top:4694px;font-size:11.5px;color:#1f2937}
.foot-nav{left:642px;top:4694px;display:flex;gap:34px;font-size:11.5px;color:var(--text)}
.foot-nav span:first-child{color:var(--ink);font-weight:500}
</style>
</head>
<body>

<header class="abs site-header">
  <div class="abs" style="left:138px;top:20px">
    <div class="brand" style="font-size:24px">Brightwell Assist</div>
    <div class="brand-sub">PUBLIC BENEFIT CORPORATION</div>
  </div>
  <nav class="abs nav"><span>Home</span><span>About Us</span><span>Our Services</span><span>Testimonials</span></nav>
  <a class="abs btn btn-orange header-cta">
    <svg width="14" height="14" viewBox="0 0 24 24" style="margin-right:10px"><path fill="#fff" d="M6.6 10.8a15 15 0 006.6 6.6l2.2-2.2c.3-.3.7-.4 1-.2 1.1.4 2.3.6 3.6.6.6 0 1 .4 1 1V20c0 .6-.4 1-1 1A17 17 0 013 4c0-.6.4-1 1-1h3.5c.6 0 1 .4 1 1 0 1.3.2 2.5.6 3.6.1.3 0 .7-.2 1z"/></svg>Contact Us</a>
</header>

<section>
  <div class="abs hero-bg" role="img" aria-label="Businessman in glasses and suit working at a laptop in a bright office"></div>
  <h1 class="abs hero-title">Empowering Your<br>Business Journey</h1>
  <p class="abs hero-text">Providing managed business services and critical support to help you navigate challenges, crises, and moments of growth</p>
  <a class="abs btn btn-orange hero-btn1">Contact Us</a>
  <a class="abs btn hero-btn2">Learn How We Can Help</a>
</section>

<div class="abs goal">OUR GOAL IS TO EMPOWER SMALL BUSINESSES WITH SERVICES AND <b>SUPPORT FOR SUCCESS.</b></div>

<section>
  <div class="abs label" style="left:138px;top:858px">Services we provide</div>
  <h2 class="abs h2 svc-head">Focused<br>Solutions for Your<br>Business Success.</h2>
  <div class="abs stat" style="left:607px"><div class="stat-num">435<small>Million</small></div><div class="stat-note">Information on 400+ million<br>companies worldwide.</div></div>
  <div class="abs stat" style="left:856px"><div class="stat-num">100<small>Percent</small></div><div class="stat-note">Overall client satisfaction<br>survey</div></div>

  <div class="abs svc-card" style="left:142px"><div class="svc-photo" role="img" aria-label="Two businessmen meeting in a modern office" style="background:linear-gradient(135deg,#cfd5d0,#6b7467)"></div><div class="svc-title">Operations Management</div><div class="svc-desc">Streamlining backend operations for smooth daily functioning</div></div>
  <div class="abs svc-card" style="left:456px"><div class="svc-photo" role="img" aria-label="Hands arranging letter blocks spelling crisis on a desk" style="background:linear-gradient(135deg,#e8e1d8,#b45a48)"></div><div class="svc-title">Crisis Intervention</div><div class="svc-desc">Immediate assistance during critical incidents to keep your business on track.</div></div>
  <div class="abs svc-card" style="left:771px"><div class="svc-photo" role="img" aria-label="Comforting hands placed together in a support session" style="background:linear-gradient(135deg,#ece7e1,#b58d77)"></div><div class="svc-title">Mental Health Support</div><div class="svc-desc">Caring for business owners and employees during stressful periods</div></div>

  <div class="abs view-all"><span class="arrow-circ"><svg width="18" height="18" viewBox="0 0 24 24"><path d="M4 12h15M13 6l6 6-6 6" stroke="#fff" stroke-width="2" fill="none"/></svg></span>View All Services</div>
  <div class="abs building" role="img" aria-label="Upward view of a tall office building"></div>
</section>

<section class="abs about"></section>
<div class="abs about-frame"></div>
<div class="abs about-photo" role="img" aria-label="Three colleagues reviewing documents together at a desk"></div>
<div class="abs about-copy">
  <div class="label">About us</div>
  <h2 class="h2" style="margin-top:12px">Brightwell Assist PBC</h2>
  <p>At Brightwell Assist PBC, we are committed to helping small business owners and entrepreneurs thrive by offering tailored business management services and critical crisis support. As a Public Benefit Corporation, we go beyond typical business solutions—our focus is on building long-term relationships that support both the professional growth and personal well-being of our clients.</p>
  <p>Through our fixed monthly fee model, we provide ongoing operational support, strategic guidance, and intervention during challenging times.</p>
  <a class="btn btn-orange" style="width:134px;height:34px;margin-top:24px">Learn More</a>
</div>

<section class="abs testi"></section>
<div class="abs testi-title"><div class="label">Client testimonials</div><h2 class="h2">What Clients Say</h2></div>
<div class="abs t-card" style="left:0;width:340px;padding-left:18px"><div class="t-name">Dana Whitfield</div><div class="t-role">Manager</div><div class="t-stars" style="left:222px">★★★★☆</div><div class="t-body">Lorem Ipsum is simply dummy text of the printing and typesetting industry. Lorem Ipsum has been the industry's standard dummy text ever since the 1500s, when an unknown printer took</div></div>
<div class="abs t-card" style="left:414px;width:381px;padding-left:60px"><div class="t-name">Lena Corwin</div><div class="t-role">Designer</div><div class="t-stars" style="left:264px">★★★★☆</div><div class="t-body">Lorem Ipsum is simply dummy text of the printing and typesetting industry. Lorem Ipsum has been the industry's standard dummy text ever since the 1500s, when an unknown printer took</div></div>
<div class="abs t-card" style="left:868px;width:332px;padding-left:60px;overflow:hidden"><div class="t-name">Theo Barnett</div><div class="t-role">CEO at Northvale Tech</div><div class="t-stars" style="left:264px">★★★★★</div><div class="t-body">Lorem Ipsum is simply dummy text of the printing and typesetting industry. Lorem Ipsum has been the industry's standard dummy text ever since the 1500s, when an unknown printer took</div></div>
<div class="abs avatar" style="left:362px" role="img" aria-label="Client portrait"></div>
<div class="abs avatar" style="left:816px" role="img" aria-label="Client portrait"></div>
<div class="abs dots"><i></i><i></i><i></i><i></i></div>

<section>
  <div class="abs why-head"><div class="label">Why choose us</div><h2 class="h2">Transforming Challenges into<br>Opportunities Together</h2></div>
  <p class="abs why-text">Brightwell Assist PBC stands apart by offering a unique fixed monthly fee model that fosters a strong, ongoing relationship with our clients. This approach allows us to provide consistent support tailored to the specific needs of small business owners and entrepreneurs, enabling them to focus on growth while we manage the complexities of their day-to-day operations.</p>
  <div class="abs feature" style="left:142px;top:2955px"><span class="f-icon f-o"><svg width="20" height="20" viewBox="0 0 24 24"><circle cx="12" cy="9" r="5" fill="none" stroke="#fff" stroke-width="2"/><path d="M3 19h18" stroke="#fff" stroke-width="2"/></svg></span>Predictable Costs</div>
  <div class="abs feature" style="left:464px;top:2955px"><span class="f-icon f-n"><svg width="20" height="20" viewBox="0 0 24 24"><circle cx="12" cy="7" r="3" fill="#fff"/><path d="M5 19c1-5 13-5 14 0z" fill="#fff"/></svg></span>Stress Reduction</div>
  <div class="abs feature" style="left:784px;top:2955px"><span class="f-icon f-o"><svg width="20" height="20" viewBox="0 0 24 24"><circle cx="15" cy="9" r="5" fill="#fff"/><path d="M3 12v8h4v-8z" fill="#fff"/></svg></span>Crisis Support Costs</div>
  <div class="abs feature" style="left:142px;top:3067px"><span class="f-icon f-n"><svg width="20" height="20" viewBox="0 0 24 24"><circle cx="12" cy="12" r="7" fill="none" stroke="#fff" stroke-width="2.5" stroke-dasharray="3 2"/><circle cx="12" cy="12" r="3" fill="#fff"/></svg></span>Personalized Solutions</div>
  <div class="abs feature" style="left:464px;top:3067px"><span class="f-icon f-o"><svg width="20" height="20" viewBox="0 0 24 24"><path d="M5 19v-5M10 19v-8M15 19v-6M20 19V6" stroke="#fff" stroke-width="2.5"/></svg></span>Facilitation Of Growth</div>
  <div class="abs feature" style="left:784px;top:3067px"><span class="f-icon f-n"><svg width="20" height="20" viewBox="0 0 24 24"><rect x="4" y="8" width="16" height="11" rx="2" fill="#fff"/><path d="M9 8V5h6v3" stroke="#fff" stroke-width="2" fill="none"/></svg></span>Enhanced Work</div>
</section>

<section class="abs contact"></section>
<div class="abs contact-head"><div class="label">Contact us</div><h2 class="h2">Reach Out Today and Let’s<br>Build Your Business Success<br>Together</h2></div>
<div class="abs map" role="img" aria-label="World map with a highlighted location"></div>
<div class="abs quote-card">
  <div class="abs quote-photo" role="img" aria-label="Smiling man and woman in glasses standing together in an office"></div>
  <form class="abs quote-form">
    <h3>Get A Free Quote Here</h3>
    <div class="field"><label>Your Name<em>*</em></label><div class="input filled">Mira Ellison |</div></div>
    <div class="field"><label>Email Address<em>*</em></label><div class="input">Enter email address</div></div>
    <div class="field"><label>Phone Number<em>*</em></label><div class="input">Enter your number</div></div>
    <div class="field"><label>Message</label><div class="input">Enter discription</div></div>
    <div class="submit">Book Appointment</div>
  </form>
</div>

<footer>
  <div class="abs foot-brand"><div class="brand">Brightwell Assist</div><div class="brand-sub">PUBLIC BENEFIT CORPORATION</div></div>
  <p class="abs foot-tag">Supporting small businesses with tailored services and crisis intervention for lasting success.</p>
  <span class="abs social" style="left:927px;background:var(--navy)"></span>
  <span class="abs social" style="left:976px;background:var(--orange)"></span>
  <span class="abs social" style="left:1024px;background:var(--navy)"></span>
  <div class="abs foot-line" style="top:4407px"></div>
  <div class="abs foot-info-title">CONTACT INFORMATIONS</div>
  <div class="abs info-col" style="left:156px"><svg width="18" height="18" viewBox="0 0 24 24"><path fill="#f97316" d="M6.6 10.8a15 15 0 006.6 6.6l2.2-2.2c.3-.3.7-.4 1-.2 1.1.4 2.3.6 3.6.6.6 0 1 .4 1 1V20c0 .6-.4 1-1 1A17 17 0 013 4c0-.6.4-1 1-1h3.5c.6 0 1 .4 1 1 0 1.3.2 2.5.6 3.6.1.3 0 .7-.2 1z"/></svg><div class="lbl">CALL US</div><div class="val">(555)-014-2876</div></div>
  <div class="abs vdiv" style="left:414px"></div>
  <div class="abs info-col" style="left:465px"><svg width="18" height="18" viewBox="0 0 24 24"><path fill="#f97316" d="M12 3l9 8h-3v9h-5v-6h-2v6H6v-9H3z"/></svg><div class="lbl">FIND US</div><div class="val">123, Lorem Ipsum is simply dummy<br>text of the printing</div></div>
  <div class="abs vdiv" style="left:782px"></div>
  <div class="abs info-col" style="left:780px"><svg width="18" height="18" viewBox="0 0 24 24"><rect x="3" y="5" width="18" height="14" rx="1" fill="#f97316"/><path d="M3 6l9 7 9-7" stroke="#fff" stroke-width="1.6" fill="none"/></svg><div class="lbl">EMAIL ADDRESS</div><div class="val">info@brightwellassist.com</div></div>
  <div class="abs foot-line" style="top:4668px"></div>
  <div class="abs copy">Copyright © 2024 Brightwell Assist | All Right Reserved.</div>
  <nav class="abs foot-nav"><span>Home</span><span>About us</span><span>Services</span><span>Testimonials</span><span>Contact Us</span></nav>
</footer>

</body>
</html>
```